TQRV Brochure

I need a one or two page brochure and I have attached the content, color pallet, format samples mimic and a couple jpeg's that are optional.

Feel free to use your judgement for graphics and style but adhere to the color schema and use our content.

Colors: You can use additional grey's, if needed.
#e23232 red
#636466 Grey
#434445 Dark grey

```html
<!DOCTYPE html>
<html lang="en">
<head>
<meta charset="utf-8">
<title>TQRV Readiness Assessment</title>
<link href="https://fonts.googleapis.com/css2?family=Poppins:wght@400;500;600;700&family=Roboto:wght@400;500&display=swap" rel="stylesheet">
<style>
  :root {
    --red: #e23232;
    --grey: #636466;
    --dark-grey: #434445;
    --navy: #1d1f35;
    --ink: #1b1b1b;
    --white: #ffffff;
    --stage: #e4e4e4;
  }
  * { margin: 0; padding: 0; box-sizing: border-box; }
  html, body { width: 1200px; height: 1200px; overflow: hidden; }
  body { background: var(--stage); font-family: "Poppins", sans-serif; position: relative; }

  .flyer { position: absolute; left: 167px; top: 40px; width: 866px; height: 1120px; background: var(--white); overflow: hidden; }

  .hero { position: absolute; left: 0; top: 0; width: 866px; height: 376px; background: var(--navy); }
  .hero-photo { position: absolute; right: 0; top: 0; width: 500px; height: 376px;
    background: radial-gradient(circle at 70% 40%, #5a4fd8 0%, #2b2f6e 35%, rgba(29,31,53,0) 70%),
                linear-gradient(100deg, var(--navy) 0%, #2a2c4a 35%, #4a5a86 70%, #8c7f79 100%); }
  .hero-photo::before { content: ""; position: absolute; left: 0; top: 0; width: 140px; height: 100%;
    background: linear-gradient(90deg, var(--navy), rgba(29,31,53,0)); }
  .seal { position: absolute; left: 55px; top: 22px; }
  .hero-title { position: absolute; left: 51px; top: 148px; color: var(--white); font-weight: 600; font-size: 41px; line-height: 43px; letter-spacing: -0.5px; }
  .hero-lede { position: absolute; left: 51px; top: 256px; width: 350px; color: var(--white); font-size: 14.5px; line-height: 20px; }

  .why-matters { position: absolute; left: 0; top: 376px; width: 866px; height: 198px; background: var(--dark-grey); border-bottom: 7px solid var(--red); }
  .tag { position: absolute; background: var(--red); color: var(--white); font-weight: 600; font-size: 17.5px; line-height: 28px; padding-left: 14px; border-radius: 0 8px 0 0; white-space: nowrap; }
  .why-matters .tag { left: 38px; top: 16px; width: 423px; }
  .cols { position: absolute; left: 51px; top: 56px; width: 770px; display: flex; gap: 26px; }
  .cols p { width: 372px; color: var(--white); font-size: 12.6px; line-height: 19.7px; letter-spacing: -0.1px; }

  .steps-tag { left: 51px; top: 611px; width: 264px; }
  .steps { position: absolute; left: 0; top: 671px; width: 866px; height: 150px; }
  .step { position: absolute; width: 250px; text-align: center; font-family: "Roboto", sans-serif; font-size: 17px; line-height: 22px; color: var(--ink); }
  .step-1 { left: 51px; } .step-2 { left: 308px; } .step-3 { left: 565px; }
  .step svg { display: block; margin: 0 auto 12px; }
  .arrow { position: absolute; top: 32px; }
  .arrow-1 { left: 228px; } .arrow-2 { left: 490px; }

  .start-tag { left: 51px; top: 850px; width: 264px; }
  .start-box { position: absolute; left: 51px; top: 878px; width: 264px; height: 173px; background: var(--dark-grey); color: var(--white); padding: 14px 12px 0 20px; font-size: 14.3px; line-height: 21.3px; }

  .edge-tag { left: 365px; top: 850px; width: 474px; }
  .edge { position: absolute; left: 376px; top: 886px; width: 480px; font-family: "Roboto", sans-serif; color: var(--ink); }
  .edge-intro, .edge-close { font-family: "Poppins", sans-serif; font-size: 14.5px; line-height: 20px; }
  .edge ul { list-style: none; margin: 8px 0 6px; }
  .edge li { font-size: 14px; line-height: 24px; display: flex; align-items: center; gap: 14px; }

  .footer { position: absolute; left: 0; top: 1051px; width: 866px; height: 69px; background: var(--red); color: var(--white); font-size: 23.5px; line-height: 69px; text-align: center; }
  .footer strong { font-weight: 600; }
</style>
</head>
<body>
<div class="flyer">
  <section class="hero">
    <div class="hero-photo" role="img" aria-label="Photo of hands typing on a laptop with glowing security shield and data panels"></div>
    <svg class="seal" width="115" height="105" viewBox="0 0 115 105" aria-hidden="true">
      <circle cx="57" cy="50" r="50" fill="#3f4aa0" stroke="#8a96e6" stroke-width="3"/>
    </svg>
    <h1 class="hero-title">TQRV Readiness<br>Assessment</h1>
    <p class="hero-lede">All vendors who aspire to work within the supply chain of the Allied Procurement Office (APO) are required to comply with the Trusted Quality Readiness Verification (TQRV). Deadlines are approaching rapidly.</p>
  </section>

  <section class="why-matters">
    <h2 class="tag">WHY DOES TQRV CERTIFICATION MATTER?</h2>
    <div class="cols">
      <p>The Trusted Quality Readiness Verification (TQRV) is designed to support businesses protect sensitive data from intellectual property theft. With cybersecurity being a key priority for the Allied Procurement Office (APO), TQRV Certification is a mandatory requirement starting 2024 for all vendors who aspire to bid on contracts and</p>
      <p>work within the supply chain of the APO. The various levels of the TQRV assure the APO that the processes and practices followed by the vendor ensure the safety of Restricted Partner Data (RPD) and Contract Record Data (CRD) and the flow of that information.</p>
    </div>
  </section>

  <h2 class="tag steps-tag">3 STEP PROCESS</h2>
  <div class="steps">
    <div class="step step-1">
      <svg width="84" height="84" viewBox="0 0 84 84" aria-hidden="true">
        <circle cx="42" cy="42" r="40" fill="#fff" stroke="#333" stroke-width="2"/>
        <rect x="22" y="25" width="40" height="27" rx="2" fill="#2f7fc4" stroke="#222" stroke-width="2"/>
        <rect x="29" y="38" width="4" height="9" fill="#f4b33a"/><rect x="35" y="33" width="4" height="14" fill="#f4b33a"/><rect x="41" y="36" width="4" height="11" fill="#fff"/>
        <circle cx="53" cy="40" r="5" fill="none" stroke="#222" stroke-width="2"/>
        <rect x="38" y="52" width="8" height="6" fill="#222"/><rect x="31" y="58" width="22" height="3" fill="#222"/>
      </svg>
      Gap Analysis
    </div>
    <svg class="arrow arrow-1" width="152" height="20" viewBox="0 0 152 20" aria-hidden="true"><path d="M0 10H148M140 3l8 7-8 7" fill="none" stroke="#111" stroke-width="2"/></svg>
    <div class="step step-2">
      <svg width="84" height="84" viewBox="0 0 84 84" aria-hidden="true">
        <circle cx="42" cy="42" r="40" fill="#fff" stroke="#333" stroke-width="2"/>
        <rect x="26" y="22" width="30" height="40" rx="2" fill="#f2f2f2" stroke="#222" stroke-width="2"/>
        <rect x="34" y="19" width="14" height="6" rx="1" fill="#2f7fc4" stroke="#222" stroke-width="1.5"/>
        <path d="M31 32h4M38 32h12M31 40h4M38 40h12M31 48h4M38 48h8" stroke="#222" stroke-width="2"/>
        <circle cx="54" cy="55" r="7" fill="#2fa05a" stroke="#222" stroke-width="1.5"/>
        <path d="M50.5 55l2.5 2.5 4.5-5" fill="none" stroke="#fff" stroke-width="2"/>
      </svg>
      Implement solutions to meet requirements
    </div>
    <svg class="arrow arrow-2" width="152" height="20" viewBox="0 0 152 20" aria-hidden="true"><path d="M0 10H148M140 3l8 7-8 7" fill="none" stroke="#111" stroke-width="2"/></svg>
    <div class="step step-3">
      <svg width="84" height="84" viewBox="0 0 84 84" aria-hidden="true">
        <circle cx="42" cy="42" r="40" fill="#fff" stroke="#333" stroke-width="2"/>
        <circle cx="42" cy="42" r="24" fill="#3f4aa0" stroke="#8a96e6" stroke-width="2"/>
      </svg>
      Get certified
    </div>
  </div>

  <h2 class="tag start-tag">HOW TO GET STARTED</h2>
  <div class="start-box">Call Norvale Systems to discuss options at 757-555-0148. Don’t hesitate as there will be a rush to certification as enforcement nears and many will be left without resources.</div>

  <h2 class="tag edge-tag">WHY NORVALE SYSTEMS</h2>
  <div class="edge">
    <p class="edge-intro">Simply put, we offer a better solution at a better price.</p>
    <ul>
      <li><svg width="20" height="12" viewBox="0 0 20 12" aria-hidden="true"><path d="M6 0l6 6-6 6-6-6z M14 0l6 6-6 6-6-6z" fill="var(--red)"/></svg>Fully Inclusive TQRV Strategy</li>
      <li><svg width="20" height="12" viewBox="0 0 20 12" aria-hidden="true"><path d="M6 0l6 6-6 6-6-6z M14 0l6 6-6 6-6-6z" fill="var(--red)"/></svg>Gap Analysis, Reporting, Affordable solutions to meet requirements.</li>
      <li><svg width="20" height="12" viewBox="0 0 20 12" aria-hidden="true"><path d="M6 0l6 6-6 6-6-6z M14 0l6 6-6 6-6-6z" fill="var(--red)"/></svg>Experienced and Certified Consultants</li>
      <li><svg width="20" height="12" viewBox="0 0 20 12" aria-hidden="true"><path d="M6 0l6 6-6 6-6-6z M14 0l6 6-6 6-6-6z" fill="var(--red)"/></svg>Local to you in Cedar Harbor, Virginia</li>
    </ul>
    <p class="edge-close">We can get you TQRV certified and save you money and time.</p>
  </div>

  <footer class="footer">For a discussion or FREE consultation, <strong>Call Us at 757-555-0148</strong></footer>
</div>
</body>
</html>
```